Unternehmensvorstellung : Broschüre DIN A4 ca. 6 Innenseiten.
Zielgruppe
Dienstleistungen:
- Messdienst und Erstellung Heiz- und Nebenkostenabrechung für Mieter
- Rauchwarnmelder Montage und Wartung
- Trinkwasser/Legionellenprüfung
- Energie-Monitoring-Service (automatisch Ermittlung günstigster Versorger)
Für:
Immobilienverwalter
Immobilienbesitzer
Immobilien Gesellschaften
Architekten und Planer
Aufgabenstellung
siehe Homepage www.wohnarcaplus.de

```html
<!DOCTYPE html>
<html lang="de">
<head>
<meta charset="utf-8">
<title>WOHNARCAplus Imagebroschüre – Doppelseite</title>
<link href="https://fonts.googleapis.com/css2?family=Barlow:wght@400;500;600;700&family=Oswald:wght@600&display=swap" rel="stylesheet">
<style>
  :root {
    --blue: #1a8ad4;
    --ink: #3a3a3a;
    --grey-w: #565656;
    --page-right: #f0f0f0;
    --white: #ffffff;
    --red: #d9412f;
    --green: #5cb531;
  }
  * { margin: 0; padding: 0; box-sizing: border-box; }
  html, body { width: 1200px; height: 424px; overflow: hidden; background: var(--white); }
  .spread { position: relative; width: 1200px; height: 424px; font-family: "Barlow", sans-serif; color: var(--ink); }
  .page { position: absolute; top: 0; height: 424px; width: 600px; overflow: hidden; }
  .page-left { left: 0; background: var(--white); }
  .page-right { left: 600px; background: var(--page-right); }

  .folio { position: absolute; top: 21px; height: 9px; background: var(--blue); color: var(--white); font-size: 4px; line-height: 9px; padding: 0 6px; }
  .folio-left { left: 0; width: 29px; }
  .folio-right { right: 0; width: 30px; }
  .running-head { position: absolute; left: 36px; top: 21px; font-size: 4px; line-height: 9px; color: #222; }
  .running-head b { font-weight: 700; }

  .page-title { position: absolute; top: 44px; color: var(--blue); font-weight: 700; font-size: 16px; letter-spacing: 0.3px; }
  .page-left .page-title { left: 37px; }
  .page-right .page-title { left: 31px; }

  .portrait { position: absolute; left: 0; top: 0; }
  .portrait-caption { position: absolute; left: 150px; top: 114px; font-size: 8px; line-height: 9.5px; color: #777; }
  .portrait-caption strong { font-weight: 600; }

  .dropcap { position: absolute; left: 290px; top: 76px; font-family: "Oswald", sans-serif; font-weight: 600; font-size: 98px; line-height: 1; color: var(--grey-w); transform: scaleX(0.82); transform-origin: left top; }
  .letter { position: absolute; left: 336px; top: 88px; width: 236px; font-size: 6.9px; line-height: 8.6px; }
  .letter p { margin-bottom: 8.6px; }
  .letter .indent { padding-left: 22px; }
  .letter .lead { padding-left: 22px; }
  .signature { width: 82px; height: 14px; background: #e6e6e6; margin: -2px 0 3px; }
  .signer { font-size: 6.9px; }

  .intro { position: absolute; left: 30px; top: 85px; width: 296px; font-size: 6.9px; line-height: 10px; text-align: justify; }
  .intro p { margin-bottom: 10px; }
  .service-list { position: absolute; left: 28px; top: 309px; font-size: 6.9px; }
  .service-list h3 { font-weight: 400; font-size: 6.9px; margin-bottom: 8px; }
  .service-list ul { list-style: none; }
  .service-list li { display: flex; align-items: center; height: 13px; padding-left: 3px; }
  .service-list svg { margin-right: 6px; }

  .visual { position: absolute; left: 0; top: 0; }
  .benefits { position: absolute; left: 330px; top: 290px; width: 270px; height: 104px; background: rgba(255,255,255,0.82); padding: 14px 0 0 5px; font-size: 6.7px; line-height: 7.2px; }
  .benefits h3 { font-size: 6.8px; font-weight: 700; letter-spacing: 0.2px; margin-bottom: 7px; }
  .benefits ul { list-style: none; }
  .benefits li { display: flex; align-items: flex-start; margin-bottom: 7.5px; padding-left: 3px; }
  .benefits li span { width: 200px; }
  .benefits svg { flex: none; margin: 1px 6px 0 0; }
</style>
</head>
<body>
<div class="spread">

  <section class="page page-left">
    <div class="folio folio-left">Seite 02</div>
    <div class="running-head"><b>WOHNARCAplus</b> MESSDIENST SERVICE IMAGEBROSCHÜRE</div>
    <h1 class="page-title">WILLKOMMEN</h1>

    <svg class="portrait" width="290" height="424" viewBox="0 0 290 424">
      <defs>
        <linearGradient id="portraitTone" x1="0" y1="0" x2="1" y2="1">
          <stop offset="0" stop-color="#b9b9b9"/>
          <stop offset="0.5" stop-color="#8a8f96"/>
          <stop offset="1" stop-color="#5d6f85"/>
        </linearGradient>
      </defs>
      <polygon role="img" aria-label="Foto des Geschäftsführers mit verschränkten Armen vor grauem Hintergrund" points="60,90 253,90 176,424 0,424 0,350" fill="url(#portraitTone)"/>
      <polygon points="253,90 268,90 191,424 176,424" fill="var(--blue)"/>
    </svg>
    <div class="portrait-caption"><strong>Max Mustermann</strong><br>Geschäftsführer</div>

    <div class="dropcap" aria-hidden="true">W</div>
    <div class="letter">
      <p class="lead" style="padding-left:22px;text-indent:0">ir die <b>WOHNARCAplus</b> geht weit über die Dienste eines klassischen Messdienstes hinaus, wir bieten mehr als Messgeräte-Vermietung und Verkauf, Hausnebenkosten- und Heizkostenabrechnung. Unser Geschäft stellt Ihnen eine große Bandbreite zur Verfügung, aus der Sie ganz nach Ihrem Geschmack wählen können.</p>
      <p class="indent">Wir besitzen eine hohe Kompetenz im Administrativen, die das Abrechnungs- und Verwaltungswesen betreffen. Eine ebenso hohe Kompetenz ist bei uns im technischen Bereich im Haus.</p>
      <p style="text-indent:22px;margin-left:-22px">Um diese Kompetenz, Flexibilität und Qualität auch in Zukunft gewährleisten zu können, arbeiten wir in allen Bereichen auch nur mit Fachfirmen zusammen. So stehen wir in sehr engem Kontakt mit unseren Lieferanten und deren Entwicklungsabteilung um auch spezielle Kundenanforderungen (Blockheizkraftwerke) erfüllen zu können und haben mit unserem Partnerunternehmen TEKAVIA eine eigene IT-Lösung entwickelt, die uns 2012 den 2.Platz des NORDTEC-Innovationspreis-IT beschert hat.</p>
      <p style="margin-left:-22px">Zukünftige Bereich: Gebäudeautomation und Sicherung<br>Ein weiteres großes Plus, ist die regionale Nähe und der persönliche Ansprechpartner. Wenn Sie mit uns in Kontakt treten, landen Sie nicht bei einem Callcenter, sondern direkt bei uns.<br>Wir sind somit bereit sehr viele Aufgaben im Immobilienbereich, die Sie an uns haben, gut aufgestellt und unterstützen Sie mit einer umfassenden und fachlich kompetenten Beratung.</p>
      <p style="margin-left:-22px">Informieren Sie sich auf unserer Internetpräsenz über unser Unternehmen und unsere Leistungen.</p>
      <div class="signature" role="img" aria-label="Handschriftliche Unterschrift" style="margin-left:-22px"></div>
      <div class="signer" style="margin-left:-22px">Max Mustermann</div>
    </div>
  </section>

  <section class="page page-right">
    <div class="folio folio-right">Seite 15</div>
    <svg class="visual" width="600" height="424" viewBox="0 0 600 424">
      <defs>
        <linearGradient id="tapTone" x1="0" y1="0" x2="1" y2="0">
          <stop offset="0" stop-color="#cfcfcf"/>
          <stop offset="0.5" stop-color="#9d9d9d"/>
          <stop offset="1" stop-color="#e4e4e4"/>
        </linearGradient>
      </defs>
      <polygon role="img" aria-label="Foto eines verchromten Wasserhahns mit fließendem Wasser vor gefliester Wand" points="378,0 600,0 600,424 291,424" fill="url(#tapTone)"/>
      <polygon points="363,0 378,0 291,424 276,424" fill="var(--blue)"/>
    </svg>

    <h2 class="page-title">Dienstleistungen im Bereich Abrechnung</h2>
    <div class="intro">
      <p>Unsere Dienstleitung im Bereiche der Abrechnung sind die Verbrauchserfassung der Wärme, Warmwasser, Kaltwasser und weitere Betriebskosten (z.B. Versicherungen, Steuern). Er umfasst die Beratung, eine ausführliche Analyse und die vollständige Erfassung und Dokumentation aller relevanten Daten Ihrer Liegenschaft.</p>
      <p>Beratung steht bei WOHNARCAplus an erster Stelle. Welches Abrechnungsverfahren ist für Sie am günstigsten? Welche Erfassungstechnik benötigen Sie dazu? Unser Außendienstmitarbeiter beantwortet Ihnen alle Fragen rund um die verursachungsgerechte Abrechnung in einem persönlichen Gespräch. Zudem analysiert er ggf. die Versorgungs- und Nutzerstruktur Ihrer Liegenschaft. Nach der Festlegung des gewünschten Dienstleistungsumfanges und der Ermittlung der optimalen Erfassungstechnik stimmen wir dann mit Ihnen weitere abrechnungstechnische Details ab. Wir erfassen und speichern für Sie alle relevanten Daten und dokumentieren alle Vereinbarungen sauber und lückenlos - Bit für Bit und Schwarz auf Weiß. Änderungen, z.B. bei Nutzern, Geräten oder dem Abrechnungszeitraum, werden von uns laufend integriert. Denn:</p>
      <p style="width:270px">Aktuelle Informationen sind das Fundament exakter Verbrauchsabrechnungen. Deshalb sollten Sie daran denken, uns rechtzeitig Änderungen bei der individuellen Versorgungs- und Nutzerstruktur Ihrer Liegenschaft mitzuteilen. Anhand der aktuellen Datenbasis erbringen wir dann regelmäßige Ablese-/Abrechnungsdienstleistungen und leiten die Ergebnisse wie im Einzelnen vereinbart an Sie weiter.</p>
    </div>

    <div class="service-list">
      <h3>Unsere Dienstleistungen in den Bereichen für die Abrechnung:</h3>
      <ul>
        <li><svg width="9" height="9" viewBox="0 0 9 9"><rect width="9" height="9" rx="1.5" fill="var(--red)"/><path d="M2 4.6 3.8 6.3 7 2.8" stroke="#fff" stroke-width="1.3" fill="none"/></svg>Erfassung und Abrechnung von Wärme</li>
        <li><svg width="9" height="9" viewBox="0 0 9 9"><rect width="9" height="9" rx="1.5" fill="var(--blue)"/><path d="M2 4.6 3.8 6.3 7 2.8" stroke="#fff" stroke-width="1.3" fill="none"/></svg>Erfassung und Abrechnung von Warmwasser</li>
        <li><svg width="9" height="9" viewBox="0 0 9 9"><rect width="9" height="9" rx="1.5" fill="var(--red)"/><path d="M2 4.6 3.8 6.3 7 2.8" stroke="#fff" stroke-width="1.3" fill="none"/></svg>Erfassung und Abrechnung von Kaltwasser</li>
        <li><svg width="9" height="9" viewBox="0 0 9 9"><rect width="9" height="9" rx="1.5" fill="var(--blue)"/><path d="M2 4.6 3.8 6.3 7 2.8" stroke="#fff" stroke-width="1.3" fill="none"/></svg>Abrechnung weiterer Betriebskosten (z.B. Versicherungen, Steuern)</li>
      </ul>
    </div>

    <aside class="benefits">
      <h3>IHRE VORTEILE AUF EINEN BLICK:</h3>
      <ul>
        <li><svg width="9" height="9" viewBox="0 0 9 9"><rect width="9" height="9" rx="1.5" fill="var(--green)"/><path d="M2 4.6 3.8 6.3 7 2.8" stroke="#fff" stroke-width="1.3" fill="none"/></svg><span>Mit unserer langjährigen Erfahrung suchen wir für Sie die optimale technische und kaufmännische Lösung.</span></li>
        <li><svg width="9" height="9" viewBox="0 0 9 9"><rect width="9" height="9" rx="1.5" fill="var(--green)"/><path d="M2 4.6 3.8 6.3 7 2.8" stroke="#fff" stroke-width="1.3" fill="none"/></svg><span>Sie haben die Sicherheit, dass alle gesetzlichen Bestimmungen eingehalten werden.</span></li>
        <li><svg width="9" height="9" viewBox="0 0 9 9"><rect width="9" height="9" rx="1.5" fill="var(--green)"/><path d="M2 4.6 3.8 6.3 7 2.8" stroke="#fff" stroke-width="1.3" fill="none"/></svg><span>Alle Vereinbarungen dokumentieren wir sauber und lückenlos, schwarz auf weiß.</span></li>
      </ul>
    </aside>
  </section>

</div>
</body>
</html>
```